Talvane Companies Business Card Design

We need a new business card for our Private Equity Real Estate Development firm, “Talvane” and our EB-5 regional center “Moorfield Regional Center” on one card. We prefer a design that is simple, elegant, and represents the luxury products we design and build as well as the financial security and stability our successful history has produced. We are an industry leader in our field and 3rd generation family business that has evolved into an institutional quality investment platform. Considered design size is standard business card dimensions (3.5 x 2 inches with an additional 1/8 inch space for design elements or backgrounds that extend beyond the finished size of your piece.

Target Market(s)

• High net worth individuals
• Highly skilled technical workers and physicians in the US seeking investment-based immigration opportunities
• Sophisticated private equity investors
• Intermediary partners include domestic attorneys and investment brokers, as well as international agent networks
• US real estate developers

Industry/Entity Type

Finance

Contact Information for Business Card

(Providing placeholder info for personal information, please design for longer character spaces, longer names and addresses etc..)
• Logo for Talvane
• Logo for Moorfield Regional Center
• Full name: Dorian Talvane
• Job title: CEO
• Email address: dtalvane@talvanecompanies.example
• Cell phone number: +1.555.318.4476
• Office number +1.555.240.6185
• Office address: Quillan Court 5, 4817 Vista Ardell, Larkmont, OR.
• Website: www.talvanecompanies.example

Font styles to use
Serif
Sans Serif

Colors
ec1f27
ffffff
000000

Requirements
Must have
• • Logo for Talvane
• • Logo for Moorfield Regional Center
• - Use rounded corners
• (See .ai file included for logos)
Nice to have
• • Simple, elegant design
• • Aesthetically compatible with our website design (www.talvanecompanies.example)
• • Color palette including but not limited to white, black, and red (as per logos)
Should not have
• - Not too much red color
• - Do not stack both logos on top of each other

```html
<!DOCTYPE html>
<html lang="en">
<head>
<meta charset="utf-8">
<title>Talvane Companies — Business Card</title>
<link href="https://fonts.googleapis.com/css2?family=Cinzel:wght@600;700&family=Arimo:wght@400&display=swap" rel="stylesheet">
<style>
  :root {
    --red: #a3162f;
    --red-deep: #8c1027;
    --ink: #2b2b2b;
    --charcoal: #333334;
    --white: #ffffff;
    --stage: #e7e7e9;
    --text: #1c1c1c;
  }
  * { box-sizing: border-box; margin: 0; padding: 0; }
  html, body { width: 1200px; height: 897px; overflow: hidden; }
  body {
    background: var(--stage);
    position: relative;
    font-family: "Arimo", Arial, sans-serif;
  }
  .card {
    position: absolute;
    left: 300px;
    width: 600px;
    height: 343px;
    background: var(--white);
    border-radius: 18px;
    overflow: hidden;
    box-shadow: 0 6px 18px rgba(0,0,0,0.18);
  }
  .card--front { top: 62px; }
  .card--back { top: 478px; }

  .footer-band {
    position: absolute;
    left: 0; right: 0; bottom: 0;
    height: 34px;
    background: linear-gradient(180deg, var(--red) 0%, var(--red-deep) 100%);
    display: flex;
    align-items: center;
    justify-content: flex-end;
    padding-right: 34px;
  }
  .website {
    color: var(--white);
    font-size: 14px;
    letter-spacing: 0.3px;
  }

  /* Front */
  .brand-front {
    position: absolute;
    left: 0; right: 0; top: 118px;
    text-align: center;
  }
  .brand-front .brand-name {
    font-family: "Cinzel", Georgia, serif;
    font-weight: 700;
    font-size: 34px;
    color: var(--red);
    letter-spacing: 1px;
    line-height: 1.2;
  }

  /* Back */
  .brand-back {
    position: absolute;
    left: 0; width: 470px; top: 58px;
    text-align: center;
  }
  .brand-back .brand-name {
    font-family: "Cinzel", Georgia, serif;
    font-weight: 700;
    font-size: 40px;
    color: var(--ink);
    letter-spacing: 1px;
  }
  .name-band {
    position: absolute;
    left: 0; right: 0; top: 170px;
    height: 48px;
    background: var(--charcoal);
  }
  .person {
    position: absolute;
    left: 0; width: 470px; top: 0; height: 48px;
    display: flex; flex-direction: column; align-items: center; justify-content: center;
    color: var(--white);
    font-family: "Cinzel", Georgia, serif;
    font-weight: 600;
  }
  .person-name { font-size: 18px; letter-spacing: 1px; line-height: 1.1; }
  .person-title { font-size: 12px; letter-spacing: 1px; line-height: 1.2; }

  .address {
    position: absolute;
    right: 30px; top: 84px;
    text-align: right;
    font-size: 14px;
    line-height: 1.35;
    color: var(--text);
    font-style: normal;
  }
  .contacts {
    position: absolute;
    left: 28px; top: 232px;
    list-style: none;
    font-size: 14px;
    color: var(--text);
  }
  .contacts li {
    display: flex; align-items: center; gap: 9px;
    height: 22px;
  }
  .contacts svg { width: 14px; height: 14px; flex: none; }
</style>
</head>
<body>

<section class="card card--front" aria-label="Card front">
  <div class="brand-front">
    <div class="brand-name">Moorfield Regional Center</div>
  </div>
  <div class="footer-band">
    <span class="website">www.talvanecompanies.example</span>
  </div>
</section>

<section class="card card--back" aria-label="Card back">
  <div class="brand-back">
    <div class="brand-name">Talvane Capital</div>
  </div>

  <address class="address">
    Quillan Court 5<br>
    4817 Vista Ardell<br>
    Larkmont, OR
  </address>

  <div class="name-band">
    <div class="person">
      <span class="person-name">DORIAN TALVANE</span>
      <span class="person-title">CEO</span>
    </div>
  </div>

  <ul class="contacts">
    <li>
      <svg viewBox="0 0 16 16" aria-hidden="true"><path fill="#a3162f" d="M3.6 1.2l2.3 2.6-1.3 1.8c.9 2 2.7 3.8 4.7 4.7l1.8-1.3 2.6 2.3-1.5 2.2C7.1 13.4 2.6 8.9 1.4 3.1z"/></svg>
      <span>+1.555.240.6185</span>
    </li>
    <li>
      <svg viewBox="0 0 16 16" aria-hidden="true"><rect x="4" y="1" width="8" height="14" rx="1.5" fill="none" stroke="#a3162f" stroke-width="1.6"/><circle cx="8" cy="12.4" r="0.9" fill="#a3162f"/></svg>
      <span>+1.555.318.4476</span>
    </li>
    <li>
      <svg viewBox="0 0 16 16" aria-hidden="true"><rect x="1" y="3" width="14" height="10" fill="#a3162f"/><path d="M1.5 3.5L8 9l6.5-5.5" fill="none" stroke="#fff" stroke-width="1.2"/></svg>
      <span>dtalvane@talvanecompanies.example</span>
    </li>
  </ul>

  <div class="footer-band">
    <span class="website">www.talvanecompanies.example</span>
  </div>
</section>

</body>
</html>
```